Dentist logo, business card and website

I have done an amateur job of creating a logo, business card and website. I would like it to look more professional. the current website can be found at www.dorenkamsel.com - I would like the website to be built and run through wix.com. The content on the website is as I would like it but I am open to suggestions.

The logo should be simple, may be best to keep to the letter DK - maybe to look like the V is a reflection of the A? Again, I am open to suggestions (I have attached a couple of images I have used on presentations but I would like the logo that you design to have a 'no fill' background so it can be placed on slides (for presentations etc).

The colour scheme seems wrong for a dentist, perhaps duck egg with black writing would be better? This applies to the business card as well (I have attached a PDF of some I have had made in the past but again they look amateur and colour scheme is wrong. The business cards should be landscape, have the logo in the top right corner, my name and qualifications in the middle, and my website and physical address in the bottom left corner: Glanmorfa Dental Surgery, 41-43 Ffordd y Bont, Cardiff CF23 9RT.

Target Market(s)

30-60 year olds

Industry/Entity Type

Dental

Contact Information for Business Card

Please see brief and uploads.

Logo Text

DK

Number of Pages Required

4 page

Font styles to use
Decorative
Script

Requirements
Must have
• A sophisticated mature feel.
Nice to have
• Simplicity.
Should not have
• Anything too complicated.

```html
<!DOCTYPE html>
<html lang="en">
<head>
<meta charset="utf-8">
<title>Doren Kamsel – Business Card</title>
<link rel="stylesheet" href="https://fonts.googleapis.com/css2?family=Cinzel:wght@600&family=EB+Garamond&family=Lato&display=swap">
<style>
  :root {
    --page: #ffffff;
    --duck-egg: #a6c9d1;
    --ink: #111111;
    --icon: #4a4f52;
  }
  * { margin: 0; padding: 0; box-sizing: border-box; }
  html, body {
    width: 1043px;
    height: 1200px;
    overflow: hidden;
    background: var(--page);
  }
  .sheet { position: relative; width: 1043px; height: 1200px; }
  .card {
    position: absolute;
    left: 44px;
    width: 956px;
    height: 547px;
    background: var(--duck-egg);
    color: var(--ink);
  }
  .card--front { top: 38px; }
  .card--back { top: 612px; }

  .brand-mark {
    position: absolute;
    display: flex;
    align-items: center;
    gap: 10px;
    font-family: "Lato", sans-serif;
    font-weight: 400;
    font-size: 28px;
    line-height: 1;
    color: var(--ink);
    transform: translate(-50%, -50%);
  }
  .brand-mark__dot {
    width: 14px;
    height: 14px;
    border-radius: 50%;
    background: var(--ink);
  }
  .card--front .brand-mark { left: 801px; top: 130px; }
  .card--back .brand-mark { left: 776px; top: 132px; }

  .identity {
    position: absolute;
    left: 0;
    width: 100%;
    text-align: center;
  }
  .card--front .identity { top: 163px; }
  .card--back .identity { top: 216px; }

  .identity__name {
    font-family: "Cinzel", serif;
    font-weight: 600;
    font-size: 54px;
    line-height: 66px;
    letter-spacing: 0;
  }
  .identity__name .initial { font-size: 66px; }
  .identity__credentials {
    font-family: "Lato", sans-serif;
    font-size: 25px;
    line-height: 30px;
    margin-top: 2px;
  }

  .contact {
    position: absolute;
    left: 90px;
    top: 320px;
    list-style: none;
    font-family: "EB Garamond", serif;
    font-size: 26px;
    line-height: 37px;
  }
  .contact__item { display: flex; align-items: flex-start; }
  .contact__icon {
    width: 22px;
    height: 22px;
    margin-top: 7px;
    margin-right: 20px;
    flex: none;
    fill: none;
    stroke: var(--icon);
    stroke-width: 1.8;
  }
  .contact__icon--solid { fill: var(--icon); stroke: none; }
</style>
</head>
<body>
<main class="sheet">
  <section class="card card--front">
    <div class="brand-mark"><span class="brand-mark__dot"></span><span>DK</span></div>
    <div class="identity">
      <h1 class="identity__name"><span class="initial">D</span>OREN <span class="initial">K</span>AMSEL</h1>
      <p class="identity__credentials">BDS (Hons) MJDF RCS (Eng)</p>
    </div>
    <ul class="contact">
      <li class="contact__item">
        <svg class="contact__icon" viewBox="0 0 24 24" aria-hidden="true">
          <path d="M12 22s-7-7.5-7-12.5a7 7 0 0 1 14 0C19 14.5 12 22 12 22z"/>
          <circle cx="12" cy="9.5" r="2.6"/>
        </svg>
        <span>Glanmorfa Dental Surgery<br>41-43 Ffordd y Bont, Cardiff&nbsp; CF23 9RT.</span>
      </li>
      <li class="contact__item">
        <svg class="contact__icon contact__icon--solid" viewBox="0 0 24 24" aria-hidden="true">
          <path d="M6.6 2.5l3 3.6-2 2.4c1.3 3 3.8 5.6 6.9 6.9l2.4-2 3.6 3-2 3.1C11 19.5 4.5 13 3.5 4.5z"/>
        </svg>
        <span>029 2048 3170</span>
      </li>
      <li class="contact__item">
        <svg class="contact__icon" viewBox="0 0 24 24" aria-hidden="true">
          <circle cx="12" cy="12" r="9"/>
          <path d="M3 12h18M12 3c3 3 3 15 0 18M12 3c-3 3-3 15 0 18M5 7.5h14M5 16.5h14"/>
        </svg>
        <span>www.dorenkamsel.com</span>
      </li>
    </ul>
  </section>

  <section class="card card--back">
    <div class="brand-mark"><span class="brand-mark__dot"></span><span>DK</span></div>
    <div class="identity">
      <h2 class="identity__name"><span class="initial">D</span>OREN <span class="initial">K</span>AMSEL</h2>
      <p class="identity__credentials">BDS (Hons) MJDF RCS (Eng)</p>
    </div>
  </section>
</main>
</body>
</html>
```